Quillmarsh Property Solutions need a business card design

Hello guys. We would need a business card design asap please.
We are a start up property investment business based in London UK specialised in buying, selling, managing and letting properties and helping distressed property owners.
The name of our Business is Quillmarsh, the logo symbolises the four fundamental elements of the world (earth, air, fire and water) and so it stands for strength, stability, longevity.
We would like the business card to communicate professionalism and reliability. Many many thanks indeed for your work.

Details:

1.) Rosalind Opaleye
Property Investor
Mobile: +44(0)7700361752
Email: rosalind.quillmarsh@brindlepost.co.uk

2.) Anselm Opaleye
Property Investor
Mobile: +44(0)7700584029
Email: anselm.quillmarsh@brindlepost.co.uk

Investment

```html
<!DOCTYPE html>
<html lang="en">
<head>
<meta charset="utf-8">
<title>Quillmarsh Property Solutions – Business Card</title>
<link rel="stylesheet" href="https://fonts.googleapis.com/css2?family=Open+Sans:wght@400;600;700&display=swap">
<style>
  :root {
    --page-bg: #e9eaee;
    --card-white: #ffffff;
    --brand-green: #3ccc72;
    --brand-red: #cc1a2c;
    --brand-blue: #1f5fcf;
    --back-blue-light: #3f86e6;
    --back-blue-dark: #1757c9;
    --ink: #111111;
    --ink-soft: #555a60;
    --divider: #b9bcc2;
  }
  * { box-sizing: border-box; margin: 0; padding: 0; }
  html, body {
    width: 1200px; height: 987px; overflow: hidden;
    background: var(--page-bg);
    font-family: "Open Sans", Arial, sans-serif;
  }
  .sheet {
    width: 1200px; height: 987px;
    display: flex; flex-direction: column; align-items: center; justify-content: center;
    gap: 48px;
  }
  .card {
    position: relative;
    width: 760px; height: 434px;
    border-radius: 26px;
    overflow: hidden;
    box-shadow: 0 10px 28px rgba(0,0,0,0.12);
  }
  .card-front { background: var(--card-white); }
  .front-art { position: absolute; inset: 0; }

  .brand {
    position: absolute; left: 44px; top: 160px;
    display: flex; align-items: center; gap: 14px;
  }
  .brand-mark {
    width: 30px; height: 30px; background: var(--brand-blue);
    flex: none;
  }
  .brand-name {
    font-weight: 700; font-size: 26px; line-height: 1.1;
    color: var(--ink); text-transform: uppercase; letter-spacing: 1px;
    width: 230px;
  }

  .person {
    position: absolute; right: 34px; top: 148px;
    text-align: right; color: var(--card-white);
  }
  .person-name { font-weight: 700; font-size: 30px; line-height: 1.2; }
  .person-role { font-weight: 400; font-size: 22px; line-height: 1.3; }

  .contact-divider {
    position: absolute; left: 176px; top: 318px;
    width: 1.5px; height: 80px; background: var(--divider);
  }
  .contacts {
    position: absolute; left: 196px; top: 326px;
    list-style: none; color: var(--ink-soft);
    font-size: 18px; line-height: 1;
  }
  .contacts li { display: flex; align-items: center; gap: 12px; margin-bottom: 16px; white-space: nowrap; }
  .contacts svg { width: 18px; height: 18px; flex: none; }

  .card-back {
    background: radial-gradient(circle at 52% 46%, var(--back-blue-light) 0%, var(--back-blue-dark) 65%);
    display: flex; flex-direction: column; align-items: center; justify-content: center;
    gap: 18px; color: var(--card-white);
  }
  .back-brand { display: flex; align-items: center; gap: 16px; }
  .back-brand .brand-mark { width: 38px; height: 38px; background: var(--card-white); }
  .back-brand-name {
    font-weight: 700; font-size: 40px; letter-spacing: 2px; text-transform: uppercase;
  }
  .web-address { font-size: 22px; letter-spacing: 3px; font-weight: 400; }
</style>
</head>
<body>
<main class="sheet">

  <section class="card card-front">
    <svg class="front-art" viewBox="0 0 760 434" width="760" height="434" aria-hidden="true">
      <path d="M0,0 H760 V434 H662 C592,230 362,62 0,60 Z" fill="var(--brand-green)"/>
      <path d="M0,66 C356,70 586,232 656,434 L626,434 C560,250 350,76 0,72 Z" fill="var(--brand-red)"/>
      <path d="M0,84 C200,86 340,120 440,176" fill="none" stroke="var(--brand-blue)" stroke-width="5"/>
    </svg>

    <div class="brand">
      <span class="brand-mark"></span>
      <span class="brand-name">Quillmarsh Property Solutions</span>
    </div>

    <div class="person">
      <p class="person-name">Rosalind Opaleye</p>
      <p class="person-role">Property Investor</p>
    </div>

    <span class="contact-divider"></span>
    <ul class="contacts">
      <li>
        <svg viewBox="0 0 18 18" aria-hidden="true">
          <rect x="4" y="1" width="10" height="16" rx="2" fill="var(--brand-blue)"/>
          <rect x="6" y="3.5" width="6" height="8" fill="var(--card-white)"/>
          <circle cx="9" cy="14.2" r="1.2" fill="var(--card-white)"/>
        </svg>
        <span>+44(0)7700361752</span>
      </li>
      <li>
        <svg viewBox="0 0 18 18" aria-hidden="true">
          <rect x="1" y="3.5" width="16" height="11" rx="2" fill="var(--brand-blue)"/>
          <path d="M2 5 L9 10 L16 5" fill="none" stroke="var(--card-white)" stroke-width="1.6"/>
        </svg>
        <span>rosalind.quillmarsh@brindlepost.co.uk</span>
      </li>
    </ul>
  </section>

  <section class="card card-back">
    <div class="back-brand">
      <span class="brand-mark"></span>
      <span class="back-brand-name">Quillmarsh</span>
    </div>
    <p class="web-address">www.quillmarshproperty.co.uk</p>
  </section>

</main>
</body>
</html>
```